New business card design needed for Trucking/Staffing company!

I am looking for a business card design. The business name is Harbor Lane Freightworks, LLC. This company is a staffing company for commercial drivers/truck drivers. Most of our customers are trucking/supply companies. Our colors are blue/black/white/grey. The info I have on my current business cards is
-Spot for a name
-2 lines for an address
-3 lines for Office, cell, and fax
-email
-website(currently on backside of card with logo but can go anywhere)
Updates

Project Deadline Extended
Reason: Open to more designs

Target Market(s)

Trucking companies, building supply companies

Industry/Entity Type

Business

Contact Information for Business Card

Edgy but professional

Font styles to use
Other font styles liked:
• Open to suggestions

Colors
0555a3
000000
ffffff
9d9d9d

Requirements
Must have
• Must have the logo incorporated

```html
<!DOCTYPE html>
<html lang="en">
<head>
<meta charset="UTF-8">
<title>Harbor Lane Freightworks — Business Card</title>
<link rel="stylesheet" href="https://fonts.googleapis.com/css2?family=Michroma&family=Raleway:wght@400&display=swap">
<style>
  :root {
    --brand-blue: #2c3f9e;
    --brand-blue-bright: #3a52c4;
    --black: #000000;
    --white: #ffffff;
    --card-grey: #3a3a3c;
    --stage: #1e1e20;
    --text-light: #f2f2f2;
  }
  * { box-sizing: border-box; margin: 0; padding: 0; }
  html, body {
    width: 1200px; height: 1200px; overflow: hidden;
    background: var(--stage);
  }
  .canvas { position: relative; width: 1200px; height: 1200px; }

  /* Front of card */
  .card-front {
    position: absolute; left: 60px; top: 250px;
    width: 400px; height: 700px;
    background: var(--card-grey);
    color: var(--text-light);
  }
  .card-front .brand-band {
    position: absolute; left: 0; top: 60px;
    width: 100%; height: 200px;
    background: var(--white);
    display: flex; align-items: center; justify-content: center;
  }
  .brand-name {
    font-family: "Michroma", sans-serif;
    font-weight: 400;
    color: var(--brand-blue);
    text-transform: uppercase;
    text-align: center;
    line-height: 1.35;
  }
  .card-front .brand-name { font-size: 22px; letter-spacing: 1px; }
  .card-front .person-name {
    position: absolute; left: 50px; top: 315px;
    font-family: "Michroma", sans-serif;
    font-size: 30px; letter-spacing: 6px;
    text-transform: uppercase;
    color: var(--white);
  }
  .card-front .contact {
    position: absolute; left: 50px;
    font-family: "Raleway", sans-serif;
    font-size: 19px; line-height: 1.55;
    text-transform: uppercase; letter-spacing: 1px;
    list-style: none;
  }
  .card-front .contact-address { top: 400px; }
  .card-front .contact-phones { top: 540px; }

  /* Back of card */
  .card-back {
    position: absolute; left: 500px; top: 417px;
    width: 640px; height: 366px;
    background: var(--black);
    display: flex; flex-direction: column;
    align-items: center; justify-content: center;
    gap: 50px;
  }
  .card-back .brand-name {
    font-size: 34px; letter-spacing: 2px;
    color: var(--brand-blue-bright);
  }
  .card-back .website {
    font-family: "Michroma", sans-serif;
    font-size: 17px; letter-spacing: 4px;
    color: var(--white);
    text-transform: uppercase;
  }
</style>
</head>
<body>
<main class="canvas">
  <section class="card-front" aria-label="Business card front">
    <div class="brand-band">
      <p class="brand-name">Harbor Lane<br>Freightworks</p>
    </div>
    <h1 class="person-name">John Doe</h1>
    <ul class="contact contact-address">
      <li>218 Quarry Ln.</li>
      <li>Corpus Christi, TX 78412</li>
      <li>dana@harborlanefw.com</li>
    </ul>
    <ul class="contact contact-phones">
      <li>T: 1(800)555-0142</li>
      <li>T: (361)555-0187</li>
      <li>F: (361)555-0193</li>
    </ul>
  </section>

  <section class="card-back" aria-label="Business card back">
    <p class="brand-name">Harbor Lane<br>Freightworks</p>
    <p class="website">www.harborlanefw.com</p>
  </section>
</main>
</body>
</html>
```